Automotive eCommerce Business looking for a business card design

Looking for a clean and simple business card design. Our company name is "Harbor Crest Auto" and we are a company specializing in the ecommerce sales of automotive parts, specifically for pick up trucks and large SUVs. Our company colours are red, black, and white.

Feel free to use the logo provided or create a new logo that you seem fit. Looking forward to your creative ideas!

Industry/Entity Type

Automotive

Contact Information for Business Card

We were thinking of a possibly two-sided design featuring just the logo and company name on one side, and personal information on the other side. Single sided designs will be considered as well.

Font styles to use
Serif
Sans Serif
Decorative

Colors
ec1f27
ffffff
000000

Requirements
Must have
• Space for employee's name, title, phone number and email address, along with the company address and website somewhere.

```html
<!DOCTYPE html>
<html lang="en">
<head>
<meta charset="utf-8">
<title>Harbor Crest Auto – Business Card</title>
<link rel="stylesheet" href="https://fonts.googleapis.com/css2?family=Roboto:wght@400;500;700&display=swap">
<style>
  :root {
    --red: #a51c22;
    --red-dark: #8c1519;
    --white: #ffffff;
    --paper: #f4f4f4;
    --ink: #2a2a2a;
    --muted: #555555;
    --stage: #3a3a3a;
  }
  * { box-sizing: border-box; margin: 0; padding: 0; }
  html, body { width: 1200px; height: 834px; overflow: hidden; }
  body {
    background: var(--stage);
    font-family: "Roboto", Arial, sans-serif;
    position: relative;
  }
  .card {
    position: absolute;
    top: 262px;
    width: 540px;
    height: 309px;
    overflow: hidden;
  }
  .card--front {
    left: 40px;
    background: linear-gradient(135deg, var(--red-dark), var(--red) 60%, var(--red-dark));
    color: var(--white);
  }
  .card--back {
    left: 620px;
    background: linear-gradient(135deg, var(--white), var(--paper));
    color: var(--ink);
  }
  .front-web {
    position: absolute;
    top: 70px;
    right: 62px;
    font-size: 13px;
    letter-spacing: 0.3px;
  }
  .front-brand {
    position: absolute;
    left: 70px;
    top: 150px;
    display: flex;
    align-items: center;
    gap: 14px;
  }
  .brand-dot {
    width: 22px;
    height: 22px;
    border-radius: 50%;
    background: var(--white);
  }
  .brand-name {
    font-size: 24px;
    font-weight: 700;
    letter-spacing: 1px;
    text-transform: uppercase;
  }
  .back-brand {
    position: absolute;
    top: 78px;
    left: 0;
    width: 100%;
    display: flex;
    justify-content: center;
    align-items: center;
    gap: 12px;
  }
  .back-brand .brand-dot { background: var(--red); }
  .back-brand .brand-name { font-size: 20px; color: var(--ink); }
  .name-band {
    position: absolute;
    top: 170px;
    left: 0;
    width: 100%;
    height: 26px;
    background: var(--red);
    color: var(--white);
    font-size: 12px;
    display: flex;
    align-items: center;
    padding-left: 190px;
  }
  .name-band strong { font-weight: 700; margin-right: 4px; }
  .contact-list {
    position: absolute;
    top: 220px;
    left: 60px;
    list-style: none;
    font-size: 11.5px;
    color: var(--muted);
  }
  .contact-list li {
    display: flex;
    align-items: center;
    gap: 10px;
    height: 22px;
  }
  .contact-list svg { width: 13px; height: 13px; }
  .divider {
    position: absolute;
    top: 212px;
    left: 300px;
    width: 1px;
    height: 70px;
    background: #bcbcbc;
  }
  .address {
    position: absolute;
    top: 222px;
    left: 330px;
    font-size: 11.5px;
    line-height: 21px;
    color: var(--muted);
  }
  .address .company { color: var(--red); text-transform: uppercase; }
</style>
</head>
<body>
  <section class="card card--front">
    <p class="front-web">www.harborcrest.com.au</p>
    <div class="front-brand">
      <span class="brand-dot"></span>
      <span class="brand-name">Harbor Crest Auto Ltd.</span>
    </div>
  </section>

  <section class="card card--back">
    <div class="back-brand">
      <span class="brand-dot"></span>
      <span class="brand-name">Harbor Crest Auto Ltd.</span>
    </div>
    <div class="name-band"><strong>Dale Morgan</strong> - President</div>

    <ul class="contact-list">
      <li>
        <svg viewBox="0 0 16 16" fill="none" stroke="#a51c22" stroke-width="1.6"><path d="M3 2h3l1.5 3.5-2 1.3a8 8 0 0 0 3.7 3.7l1.3-2L14 10v3a1 1 0 0 1-1 1A12 12 0 0 1 2 3a1 1 0 0 1 1-1z"/></svg>
        555-014-2876
      </li>
      <li>
        <svg viewBox="0 0 16 16" fill="none" stroke="#a51c22" stroke-width="1.6"><rect x="1.5" y="3.5" width="13" height="9"/><path d="M1.5 3.5 8 9l6.5-5.5"/></svg>
        dale@harborcrest.com.au
      </li>
      <li>
        <svg viewBox="0 0 16 16" fill="none" stroke="#a51c22" stroke-width="1.6"><circle cx="8" cy="8" r="6.5"/><path d="M1.5 8h13M8 1.5c3 3.5 3 9.5 0 13M8 1.5c-3 3.5-3 9.5 0 13"/></svg>
        www.harborcrest.com.au
      </li>
    </ul>

    <div class="divider"></div>

    <address class="address">
      <span class="company">Harbor Crest Auto Ltd.</span><br>
      48 Marlow Street<br>
      2nd Floor Eastport
    </address>
  </section>
</body>
</html>
```